Etiketten-Design für Eierschachtel
Zielgruppe
Wir haben einen Hofladen, indem wir unsere hofeigenen Produkte direkt an den Verbraucher verkaufen.
Aufgabenstellung
Wir suchen ein Etikett für unsere Eierschachtel, die wir für den Verkauf unserer Eier im eigenen Hofladen benötigen.
Das Etikett soll hell und freundlich, aber keinesfalls überladen oder zu verspielt sein. Es soll die Natürlichkeit und Regionalität widerspiegeln. Wir halten unsere Hühner in mobiler Freilandhaltung mit ausreichend Auslauf auf unseren Wiesen.
Das beigefügte Logo (einmal farbig, einmal schwarz/weiß - je nach Vorschlag was besser passt) soll integriert werden.
Das Etikett soll folgende Punkte enthalten:
Rückseite:
- 'Verbraucherhinweis: Nach dem Kauf bei Kühlschranktemperatur aufbewahren. Nach Ablauf des
Mindesthaltbarkeitsdatums durcherhitzen.'
- Familie Haslbeck
Lindenweg 7
84273 Moosreith
Vorderseite (zum Öffnen der Eierschachtel) bzw. Deckel oben:
- '10 frische Eier aus mobiler Freilandhaltung' (gerne auch eigene Vorschläge von Ihnen)
- passender Slogan, der auf Regionalität bzw. Einkaufen direkt beim Erzeuger basiert
Format: ca. 21,4cm breit und ca. 14,2cm lang

```html
<!DOCTYPE html>
<html lang="de">
<head>
<meta charset="utf-8">
<title>Etikett Eierschachtel – Haslbeck Hof</title>
<link rel="stylesheet" href="https://fonts.googleapis.com/css2?family=Arimo:wght@400&family=Source+Sans+3:wght@400;600;700&family=Open+Sans:wght@600;700&display=swap">
<style>
  :root{
    --page:#f0f0f0;
    --cut:#1aa3d4;
    --bleed:#c8287f;
    --measure:#d9534f;
    --back-panel:#eef3ec;
    --front-panel:#f5e6d8;
    --note-green:#5c9d58;
    --brand-green:#2e7d32;
    --banner-brown:#7a2e0a;
    --slogan-brown:#a97a4e;
    --egg-brown:#6b2a0c;
    --white:#ffffff;
  }
  html,body{margin:0;padding:0;overflow:hidden;background:var(--page);}
  .sheet{position:relative;width:1200px;height:872px;overflow:hidden;background:var(--page);font-family:"Source Sans 3",sans-serif;}
  .dieline{position:absolute;left:0;top:0;}
  .back-note{position:absolute;transform:rotate(180deg);color:var(--note-green);font-size:10.5px;line-height:14px;letter-spacing:.2px;}
  .back-note .heading{font-weight:700;font-size:12.5px;line-height:16px;text-decoration:underline;text-underline-offset:3px;}
  .back-note--usage{left:154px;top:223px;width:292px;}
  .back-note--address{left:750px;top:223px;width:108px;}
  .brand{position:absolute;left:120px;top:410px;width:232px;text-align:center;}
  .brand-ring{width:102px;height:102px;margin:0 auto 12px;border:1.5px solid var(--brand-green);border-radius:50%;}
  .brand-name{font-size:28px;font-weight:600;color:var(--brand-green);letter-spacing:.5px;line-height:1;}
  .banner{position:absolute;left:334px;top:420px;width:364px;height:74px;background:var(--banner-brown);color:var(--white);box-sizing:border-box;padding:6px 0 0 18px;}
  .banner-title{font-family:"Open Sans",sans-serif;font-weight:700;font-size:35px;line-height:38px;letter-spacing:-.6px;white-space:nowrap;}
  .banner-sub{font-family:"Open Sans",sans-serif;font-weight:600;font-size:17px;line-height:21px;letter-spacing:-.2px;white-space:nowrap;}
  .egg-count{position:absolute;left:820px;top:578px;width:95px;text-align:center;color:var(--egg-brown);}
  .egg-count .number{font-family:"Open Sans",sans-serif;font-weight:700;font-size:46px;line-height:48px;}
  .egg-count .label{font-family:"Open Sans",sans-serif;font-weight:700;font-size:10.5px;line-height:14px;}
  .slogan{position:absolute;left:280px;top:677px;width:490px;text-align:center;color:var(--slogan-brown);font-family:"Open Sans",sans-serif;font-weight:700;}
  .slogan .small{font-size:20px;line-height:26px;}
  .slogan .big{font-size:33px;line-height:38px;}
  .measure-label{position:absolute;color:var(--measure);font-size:16px;line-height:18px;font-family:"Arimo",sans-serif;white-space:nowrap;}
  .measure-label.vertical{transform:rotate(-90deg);transform-origin:center;}
</style>
</head>
<body>
<div class="sheet">
  <svg class="dieline" width="1200" height="872" viewBox="0 0 1200 872">
    <defs>
      <clipPath id="label-shape">
        <path d="M129,177 H924 Q932,177 932,185 V318 Q932,340 952,345 Q968,348 968,360 V580 Q968,592 950,596 Q932,600 932,615 V640 Q932,650 920,651 H805 Q788,652 784,670 L778,756 Q777,766 767,766 H291 Q282,766 281,756 L276,705 Q272,660 245,652 H132 Q121,652 121,640 V615 Q121,600 103,596 Q83,592 83,580 V360 Q83,348 99,345 Q121,340 121,318 V185 Q121,177 129,177 Z"/>
      </clipPath>
      <linearGradient id="meadow" x1="0" y1="0" x2="1" y2="0">
        <stop offset="0" stop-color="#dcdcd6"/>
        <stop offset=".3" stop-color="#c9d0bc"/>
        <stop offset=".52" stop-color="#86ad66"/>
        <stop offset=".72" stop-color="#a5652c"/>
        <stop offset=".84" stop-color="#b5702f"/>
        <stop offset="1" stop-color="#7fb05c"/>
      </linearGradient>
    </defs>

    <g clip-path="url(#label-shape)">
      <rect class="panel-back" x="60" y="150" width="940" height="172" fill="var(--back-panel)"/>
      <rect class="photo-meadow" x="60" y="322" width="940" height="330" fill="url(#meadow)" role="img" aria-label="Foto: braunes Huhn auf grüner Wiese in Freilandhaltung"/>
      <rect class="panel-front" x="60" y="652" width="940" height="130" fill="var(--front-panel)"/>
    </g>

    <path class="egg-shape" d="M867,548 C895,548 912,590 912,622 C912,645 895,652 867,652 C839,652 822,645 822,622 C822,590 839,548 867,548 Z" fill="#f4f1ec"/>

    <path class="bleed-line" fill="none" stroke="var(--bleed)" stroke-width="2" d="M129,177 H924 Q932,177 932,185 V318 Q932,340 952,345 Q968,348 968,360 V580 Q968,592 950,596 Q932,600 932,615 V640 Q932,650 920,651 H805 Q788,652 784,670 L778,756 Q777,766 767,766 H291 Q282,766 281,756 L276,705 Q272,660 245,652 H132 Q121,652 121,640 V615 Q121,600 103,596 Q83,592 83,580 V360 Q83,348 99,345 Q121,340 121,318 V185 Q121,177 129,177 Z"/>
    <path class="cut-line" fill="none" stroke="var(--cut)" stroke-width="2" d="M110,156 H944 Q954,156 954,166 V312 Q954,332 972,336 Q992,340 992,352 V588 Q992,600 974,604 Q954,608 954,622 V652 Q954,662 944,662 H812 Q800,662 796,680 L786,778 Q785,786 776,786 H278 Q270,786 269,778 L262,705 Q258,672 240,662 H110 Q100,662 100,652 V622 Q100,608 82,604 Q60,600 60,588 V352 Q60,340 78,336 Q100,332 100,312 V166 Q100,156 110,156 Z"/>

    <g class="measures" stroke="var(--measure)" stroke-width="1" fill="none">
      <line x1="84" y1="98" x2="971" y2="98"/>
      <line x1="84" y1="92" x2="84" y2="330"/><line x1="971" y1="92" x2="971" y2="330"/>
      <line x1="122" y1="135" x2="933" y2="135"/>
      <line x1="122" y1="130" x2="122" y2="170"/><line x1="933" y1="130" x2="933" y2="170"/>
      <line x1="273" y1="804" x2="782" y2="804"/>
      <line x1="273" y1="770" x2="273" y2="818"/><line x1="782" y1="770" x2="782" y2="818"/>
      <line x1="1016" y1="180" x2="1016" y2="766"/>
      <line x1="1067" y1="180" x2="1067" y2="766"/>
      <line x1="936" y1="180" x2="1075" y2="180"/>
      <line x1="970" y1="347" x2="1026" y2="347"/>
      <line x1="970" y1="594" x2="1026" y2="594"/>
      <line x1="782" y1="766" x2="1075" y2="766"/>
      <circle cx="225" cy="698" r="47" stroke="#e07a74"/>
    </g>
    <g class="radius-marks" fill="#c0c0c4" stroke="#a8a8ae">
      <circle cx="96" cy="582" r="12"/>
      <circle cx="134" cy="638" r="12"/>
      <circle cx="294" cy="754" r="12"/>
    </g>
  </svg>

  <div class="back-note back-note--usage">
    <div class="heading">Verbraucherhinweis:</div>
    <div>Nach dem Kauf bei Kühlschranktemperatur aufbewahren.</div>
    <div>Nach Ablauf des Mindesthaltbarkeitsdatums durcherhitzen.</div>
  </div>
  <div class="back-note back-note--address">
    <div class="heading">Familie Haslbeck</div>
    <div>Lindenweg 7</div>
    <div>84273 Moosreith</div>
  </div>

  <div class="brand">
    <div class="brand-ring"></div>
    <div class="brand-name">HASLBECK HOF</div>
  </div>

  <div class="banner">
    <div class="banner-title">FRISCHE EIER AUS</div>
    <div class="banner-sub">MOBILER FREILANDHALTUNG</div>
  </div>

  <div class="egg-count">
    <div class="number">10</div>
    <div class="label">FRISCHE EIER</div>
  </div>

  <div class="slogan">
    <div class="small">Weil's regional</div>
    <div class="big">am besten ist</div>
  </div>

  <div class="measure-label" style="left:497px;top:74px;">214 mm</div>
  <div class="measure-label" style="left:497px;top:111px;">196 mm</div>
  <div class="measure-label" style="left:497px;top:814px;">123mm</div>
  <div class="measure-label vertical" style="left:997px;top:255px;">40.5 mm</div>
  <div class="measure-label vertical" style="left:1004px;top:463px;">60 mm</div>
  <div class="measure-label vertical" style="left:997px;top:672px;">41.5 mm</div>
  <div class="measure-label vertical" style="left:1050px;top:465px;">142 mm</div>
  <div class="measure-label" style="left:117px;top:572px;">R = 6 mm</div>
  <div class="measure-label" style="left:152px;top:629px;">R = 6 mm</div>
  <div class="measure-label" style="left:285px;top:690px;">R = 23 mm</div>
  <div class="measure-label" style="left:313px;top:746px;">R = 6 mm</div>
</div>
</body>
</html>
```